Business Card Design

We are a florist shop that also stocks a range of giftware and jewellery. I would like a new design that incorporates a light green background. If you could use a skeleton leaf somewhere in the design that would be great. I would also like to incorporate the find us on Chatterlink logo on this design.

Industry/Entity Type

Florist

Contact Information for Business Card

Petals at Harwick
42 Tellbury street
Wrenford Ashvale 3942
Phone: 0352984407
Fax : 0352984433
email: pah@brightmail.net.au

Proprietors : Dana & Lou Fenwright

```html
<!DOCTYPE html>
<html lang="en">
<head>
<meta charset="utf-8">
<title>Petals at Harwick – Business Card</title>
<link href="https://fonts.googleapis.com/css2?family=Sorts+Mill+Goudy&display=swap" rel="stylesheet">
<style>
  :root {
    --page: #ffffff;
    --frame: #1a1a1a;
    --leaf-pale: #eef2dc;
    --leaf-light: #dde4bf;
    --leaf-mid: #c7d194;
    --leaf-deep: #a5b55c;
    --flourish: #c4cb9c;
    --ink: #86876a;
  }
  * { margin: 0; padding: 0; box-sizing: border-box; }
  html, body {
    width: 1200px;
    height: 806px;
    overflow: hidden;
    background: var(--page);
  }
  .canvas {
    position: relative;
    width: 1200px;
    height: 806px;
    border: 2px solid var(--frame);
    background: var(--page);
  }
  .business-card {
    position: absolute;
    left: 115px;
    top: 107px;
    width: 993px;
    height: 601px;
    overflow: hidden;
  }
  .card-background {
    position: absolute;
    inset: 0;
    width: 100%;
    height: 100%;
  }
  .flourish-area {
    position: absolute;
    left: 0;
    top: 0;
  }
  .contact-block {
    position: absolute;
    left: 399px;
    top: 279px;
    font-family: "Sorts Mill Goudy", "Goudy Bookletter 1911", serif;
    font-style: normal;
    font-size: 33px;
    line-height: 47.5px;
    letter-spacing: 0.8px;
    color: var(--ink);
    white-space: nowrap;
  }
  .social-link {
    position: absolute;
    right: 46px;
    bottom: 12px;
    display: flex;
    align-items: center;
    gap: 12px;
    font-family: "Sorts Mill Goudy", "Goudy Bookletter 1911", serif;
    font-size: 28px;
    line-height: 40px;
    color: var(--ink);
    white-space: nowrap;
  }
  .social-mark {
    width: 30px;
    height: 30px;
    background: var(--ink);
  }
</style>
</head>
<body>
<div class="canvas">
  <div class="business-card">
    <svg class="card-background" viewBox="0 0 993 601" preserveAspectRatio="none" aria-hidden="true">
      <defs>
        <linearGradient id="lower-wash" x1="0" y1="0" x2="1" y2="0">
          <stop offset="0" stop-color="var(--leaf-pale)"/>
          <stop offset="0.45" stop-color="var(--leaf-mid)"/>
          <stop offset="1" stop-color="var(--leaf-deep)"/>
        </linearGradient>
        <linearGradient id="upper-wash" x1="0" y1="0" x2="1" y2="0">
          <stop offset="0" stop-color="#e4e9c8"/>
          <stop offset="1" stop-color="var(--leaf-light)"/>
        </linearGradient>
      </defs>
      <rect class="lower-band" width="993" height="601" fill="url(#lower-wash)"/>
      <path class="upper-swoosh" d="M0 0 H993 V246 C760 262 430 228 210 110 C130 68 70 30 20 0 Z" fill="url(#upper-wash)"/>
    </svg>

    <svg class="flourish-area" role="img" aria-label="Floral flourish of swirling stems, leaves and blossoms rising from the lower left corner" viewBox="0 0 400 601" width="400" height="601">
      <defs>
        <radialGradient id="flourish-tone" cx="0.3" cy="0.6" r="0.75">
          <stop offset="0" stop-color="var(--flourish)" stop-opacity="0.75"/>
          <stop offset="1" stop-color="var(--flourish)" stop-opacity="0"/>
        </radialGradient>
      </defs>
      <rect width="400" height="601" fill="url(#flourish-tone)"/>
    </svg>

    <address class="contact-block">
      <div class="business-name">Petals at Harwick 42,</div>
      <div class="street-address">Tellbury street Wrenford Ashvale 3942</div>
      <div class="phone-fax">Phone: 0352984407 Fax : 0352984433</div>
      <div class="email">email: pah@brightmail.net.au</div>
      <div class="proprietors">Proprietors : Dana &amp; Lou Fenwright</div>
    </address>

    <div class="social-link">
      <span class="social-label">Find us on Chatterlink</span>
      <span class="social-mark"></span>
    </div>
  </div>
</div>
</body>
</html>
```